Popup Banners - BrightCounsel - Legal Technology

- We need two banners (same style) designed with two different images and different text.

- The details of the printing requirements are attached, along with suggested images.

- The banners should share the same theme as our website www.brightcounsel.com.au

- The first banner would include our logo (attached), use the 'roads join' image (attached) in some way and text: New Opportunities - Where legal services and technology meet.

- The second banner would include our logo (attached), use the 'jigsaw' image (attached) in some way and use text: Legal Technology Strategy, Advice and Capability.

- Details on what are required from the Printer is attached also.

Target Market(s)

Legal Professionals

Industry/Entity Type

Information Technology

Font styles to use
Sans Serif

Requirements
Must have
• Our logo (attached), suggested text and the image mentioned for each.
Nice to have
• Professional and modern look
Should not have
• Cheap looking

```html
<!DOCTYPE html>
<html lang="en">
<head>
<meta charset="utf-8">
<title>BrightCounsel – Legal Technology Banner</title>
<link href="https://fonts.googleapis.com/css2?family=Dosis:wght@400;500&display=swap" rel="stylesheet">
<style>
  :root {
    --page-bg: #ffffff;
    --navy-deep: #141c27;
    --navy: #1d3550;
    --steel: #3f6f98;
    --ice: #cfe6f6;
    --glow: #eef7fd;
    --band: rgba(20, 26, 35, 0.86);
    --text-light: #ffffff;
  }
  html, body {
    margin: 0;
    padding: 0;
    width: 1042px;
    height: 1200px;
    overflow: hidden;
    background: var(--page-bg);
  }
  .canvas {
    position: relative;
    width: 1042px;
    height: 1200px;
    display: flex;
    align-items: center;
    justify-content: center;
  }
  .banner {
    position: relative;
    width: 470px;
    height: 1160px;
    overflow: hidden;
    background: var(--navy-deep);
    font-family: "Dosis", sans-serif;
    color: var(--text-light);
  }
  .banner__photo {
    position: absolute;
    inset: 0;
    background:
      radial-gradient(ellipse 60% 18% at 55% 28%, var(--glow) 0%, rgba(207,230,246,0.7) 35%, rgba(63,111,152,0) 75%),
      radial-gradient(ellipse 45% 14% at 80% 52%, rgba(238,247,253,0.9) 0%, rgba(63,111,152,0) 70%),
      radial-gradient(ellipse 50% 16% at 45% 70%, rgba(238,247,253,0.95) 0%, rgba(63,111,152,0) 70%),
      linear-gradient(180deg, var(--steel) 0%, var(--navy) 45%, var(--steel) 70%, var(--navy) 100%);
  }
  .banner__top {
    position: absolute;
    top: 0; left: 0; right: 0;
    height: 102px;
    background: var(--band);
    display: flex;
    align-items: center;
    padding-left: 45px;
  }
  .brand-name {
    font-size: 20px;
    font-weight: 500;
    letter-spacing: 0.32em;
    color: var(--text-light);
  }
  .headline {
    position: absolute;
    left: 45px;
    top: 820px;
    margin: 0;
    font-weight: 400;
    font-size: 51px;
    line-height: 64px;
    letter-spacing: -0.01em;
  }
  .banner__bottom {
    position: absolute;
    left: 0; right: 0; bottom: 0;
    height: 135px;
    background: var(--band);
    display: flex;
    justify-content: center;
    padding-top: 34px;
    box-sizing: border-box;
  }
  .web-address {
    font-size: 13px;
    font-weight: 500;
    letter-spacing: 0.02em;
  }
</style>
</head>
<body>
  <main class="canvas">
    <article class="banner">
      <div class="banner__photo" role="img" aria-label="Backlit jigsaw puzzle pieces in cool blue light, a fingertip placing the last piece"></div>
      <header class="banner__top">
        <span class="brand-name">BrightCounsel</span>
      </header>
      <h1 class="headline">Legal Technology<br>Strategy, Advice<br>and Capability</h1>
      <footer class="banner__bottom">
        <span class="web-address">www.brightcounsel.com.au</span>
      </footer>
    </article>
  </main>
</body>
</html>
```